Professional DJ Business Card

Business card for giving out to clubs and venues or interested groups that are in need of a professional DJ. I want something artistic and catchy/alluring, with a minimalist approach that gets just the vital amount of info and leaves the rest for inquiry via contacting me. Ideally I would like one side to have an image of something cool like an eye and my name, then the other side be the contact info, I am definitely feeling a black or dark colored card, but I am open to other designs. I am uploading a picture that I made that reflects a little of what I am *kind of* looking for.

Industry/Entity Type

Business

Contact Information for Business Card

Tomas Halvik (Nuvrik)
Professional DJ (West Coast)
EDM (Deep/House/Techno), Hip Hop, Latin, Trap.
Cell: 555-274-9163
Email: Nuvrikofficial@mailnest.net
www.beatcloudia.net/yourtuneisfading

```html
<!DOCTYPE html>
<html lang="en">
<head>
<meta charset="utf-8">
<title>Nuvrik – DJ Business Card</title>
<link rel="stylesheet" href="https://fonts.googleapis.com/css2?family=Overpass+Mono:wght@500;600&display=swap">
<style>
  :root {
    --card-bg: #0c0c0d;
    --ink: #ffffff;
    --divider: #2f3634;
  }
  html, body {
    margin: 0;
    padding: 0;
    width: 1200px;
    height: 702px;
    overflow: hidden;
    background: var(--card-bg);
  }
  .card {
    position: relative;
    width: 1200px;
    height: 702px;
    background: var(--card-bg);
    color: var(--ink);
    font-family: "Overpass Mono", monospace;
    text-transform: uppercase;
  }
  .contact-block {
    position: absolute;
    left: 71px;
    top: 52px;
    margin: 0;
    font-size: 37px;
    font-weight: 600;
    line-height: 51px;
    letter-spacing: 7px;
    white-space: nowrap;
  }
  .contact-block p {
    margin: 0;
  }
  .divider {
    position: absolute;
    left: 0;
    top: 510px;
    width: 1200px;
    height: 6px;
    background: var(--divider);
  }
  .brand-name {
    position: absolute;
    left: 0;
    top: 566px;
    width: 1200px;
    margin: 0;
    text-align: center;
    font-size: 88px;
    line-height: 1;
    font-weight: 500;
    letter-spacing: 10px;
    padding-left: 10px;
    box-sizing: border-box;
  }
</style>
</head>
<body>
  <main class="card">
    <section class="contact-block">
      <p class="contact-name">Tomas Halvik (Nuvrik)</p>
      <p class="contact-role">Professional DJ (West Coast)</p>
      <p class="contact-genres">EDM (Deep/House/Techno), Hip Hop,</p>
      <p class="contact-genres">Latin, Trap.</p>
      <p class="contact-phone">Cell: 555-274-9163</p>
      <p class="contact-email">Email: Nuvrikofficial@mailnest.net</p>
      <p class="contact-web">www.beatcloudia.net/yourtuneisfading</p>
    </section>
    <div class="divider"></div>
    <h1 class="brand-name">Nuv Rik</h1>
  </main>
</body>
</html>
```